Real Estate Entrepreneur needs a business card

I am a real estate entrepreneur, I buy houses for investment purposes, I act as a real estate agent representing buyers and sellers in residential home transactions, I am a contractor that does a wide range of home repairs and construction. I'd like a design that can stick with me through the years as my business grows and morphs to fit any niche I decide to pursue as markets change.

Target Market(s)

Anyone with interest that may be related to real estate.

Industry/Entity Type

Real Estate

Contact Information for Business Card

A card that stands out and doesn't put me in any one box. My business will evolve over time and I need a card that can stay relevant.

Colors

Designer to choose colors to be used in the design.

Requirements
Must have
• Character
Nice to have
• I'm open
Should not have
• Cliche houses and hammers

```html
<!DOCTYPE html>
<html lang="en">
<head>
<meta charset="UTF-8">
<title>Ross Hale – Business Card</title>
<link href="https://fonts.googleapis.com/css2?family=Michroma&family=Open+Sans:wght@400;600&display=swap" rel="stylesheet">
<style>
  :root {
    --canvas-bg: #d9dadd;
    --card-white: #ffffff;
    --card-white-fade: #eef0f3;
    --ink-dark: #2b2e33;
    --ink-mid: #6f7379;
    --ink-soft: #8c9096;
    --navy-deep: #0f161d;
    --navy-mid: #1f2a35;
    --navy-light: #3c4a58;
    --accent: #2f3d63;
    --text-light: #ffffff;
  }
  * { box-sizing: border-box; margin: 0; padding: 0; }
  html, body { width: 1200px; height: 1200px; overflow: hidden; }
  body {
    background: var(--canvas-bg);
    position: relative;
    font-family: "Open Sans", sans-serif;
  }
  .card {
    position: absolute;
    top: 270px;
    width: 380px;
    height: 660px;
    box-shadow: 0 18px 40px rgba(0,0,0,0.18);
    overflow: hidden;
  }
  .card-front {
    left: 180px;
    background: linear-gradient(180deg, var(--card-white) 55%, var(--card-white-fade) 100%);
    padding: 150px 40px 50px 44px;
  }
  .card-back {
    left: 640px;
    background: linear-gradient(160deg, var(--navy-light) 0%, var(--navy-mid) 30%, var(--navy-deep) 75%);
    display: flex;
    align-items: center;
    padding-left: 70px;
  }
  .skyline-fade {
    position: absolute;
    right: 30px;
    bottom: 0;
    width: 170px;
    height: 430px;
    background: linear-gradient(180deg, rgba(220,224,230,0) 0%, rgba(210,215,222,0.55) 60%, rgba(205,210,218,0.7) 100%);
  }
  .back-fade {
    position: absolute;
    right: 0;
    bottom: 0;
    width: 220px;
    height: 380px;
    background: linear-gradient(180deg, rgba(60,74,88,0) 0%, rgba(60,74,88,0.35) 100%);
  }
  .brand-row { display: flex; align-items: center; gap: 12px; position: relative; }
  .brand-mark { width: 14px; height: 14px; background: var(--accent); }
  .brand-name {
    font-family: "Michroma", sans-serif;
    font-size: 31px;
    letter-spacing: 1px;
    color: var(--ink-dark);
    line-height: 1;
  }
  .role {
    position: relative;
    margin-top: 10px;
    font-size: 15px;
    line-height: 1.45;
    color: var(--ink-soft);
  }
  .role .role-main { font-weight: 600; }
  .contact {
    position: absolute;
    left: 110px;
    bottom: 50px;
    font-size: 15.5px;
    color: var(--ink-mid);
  }
  .contact-list { list-style: none; }
  .contact-list li { display: flex; align-items: center; gap: 8px; line-height: 1.6; }
  .contact-list svg { width: 13px; height: 13px; flex: none; }
  .address { margin-top: 18px; line-height: 1.35; }
  .website {
    margin-top: 12px;
    font-weight: 600;
    letter-spacing: 0.5px;
    color: var(--ink-dark);
  }
  .back-name {
    position: relative;
    font-family: "Michroma", sans-serif;
    font-size: 44px;
    line-height: 1.25;
    letter-spacing: 2px;
    color: var(--text-light);
  }
</style>
</head>
<body>

  <section class="card card-front">
    <div class="skyline-fade" role="img" aria-label="Faint skyline decoration in soft grey"></div>
    <div class="brand-row">
      <span class="brand-mark"></span>
      <h1 class="brand-name">ROSS HALE</h1>
    </div>
    <p class="role"><span class="role-main">Real Estate Entrepreneur</span><br>contractor</p>

    <div class="contact">
      <ul class="contact-list">
        <li>
          <svg viewBox="0 0 12 12" aria-hidden="true"><rect x="0.5" y="0.5" width="11" height="11" fill="none" stroke="#6f7379"/><path d="M3 4h6v4H3z" fill="#6f7379"/></svg>
          1-234-567890
        </li>
        <li>
          <svg viewBox="0 0 12 12" aria-hidden="true"><rect x="0.5" y="0.5" width="11" height="11" fill="none" stroke="#6f7379"/><rect x="4" y="2.5" width="4" height="7" rx="0.8" fill="#6f7379"/></svg>
          1-234-567890
        </li>
        <li>
          <svg viewBox="0 0 12 12" aria-hidden="true"><rect x="0.5" y="0.5" width="11" height="11" fill="none" stroke="#6f7379"/><path d="M2.5 3.5h7v5h-7z" fill="#6f7379"/><path d="M2.5 3.5l3.5 3 3.5-3" fill="none" stroke="#fff" stroke-width="0.8"/></svg>
          ross@halehomes.com
        </li>
      </ul>
      <p class="address">Dummy city<br>Dummy Country Land</p>
      <p class="website">www.halehomes.com</p>
    </div>
  </section>

  <section class="card card-back">
    <div class="back-fade" role="img" aria-label="Soft textured skyline shading in dark slate"></div>
    <h2 class="back-name">ROSS<br>HALE</h2>
  </section>

</body>
</html>
```